Velmora web stylesheet and logo

We are developing a new site for Velmora and would like someone to provide a new logo and a web page style guide.
This company connects carriers with with customers that need specialty moves: store fixtures, displays, exhibits, technology, manufacturing equipment, etc.
We want to convey quality customer service, quality transportation, and the use of current technology in our business. We do not want to look like a trucking company.
Logo needs a total remake!!!

Target Market(s)

Technology, Retail, Manufacturing, Hospitalty...

Industry/Entity Type

It Company

Logo Text

we will provide some thing soon

Number of Pages Required

1 page

Font styles to use
Serif
Sans Serif

Requirements
Must have
• Warm colors, professional looking.
Nice to have
• If you have pics to include we'll consider
Should not have
• We must no look like a trucking company.

```html
<!DOCTYPE html>
<html lang="en">
<head>
<meta charset="utf-8">
<title>Velmora — Specialty Moves</title>
<link rel="stylesheet" href="https://fonts.googleapis.com/css2?family=Open+Sans:ital,wght@0,400;0,600;0,700;0,800;1,700;1,800&display=swap">
<style>
:root{
  --blue:#0b5f96;
  --blue-dark:#084a76;
  --red:#9c0d0d;
  --red-bright:#b3151a;
  --ink:#2a2a2a;
  --muted:#555;
  --grey:#ececec;
  --grey-2:#f4f4f4;
  --rule:#cfcfcf;
  --white:#fff;
  --footer-bar:#1d1d1d;
}
*{box-sizing:border-box;margin:0;padding:0}
html,body{width:1200px;height:3203px;overflow:hidden}
body{font-family:"Open Sans",Arial,sans-serif;color:var(--ink);background:var(--white);position:relative}
.abs{position:absolute}
section,header,footer,nav{position:absolute;left:0;width:1200px}

/* header */
.site-header{top:0;height:123px;background:var(--white)}
.top-rule{left:0;top:0;width:720px;height:4px;background:var(--blue)}
.contact-strip{left:718px;top:0;width:482px;height:34px;background:var(--blue);border-bottom-left-radius:18px;display:flex;align-items:center;gap:26px;padding-left:30px;color:var(--white);font-size:13px;font-weight:600}
.contact-strip .item{display:flex;align-items:center;gap:8px}
.socials{display:flex;gap:4px;margin-left:auto;margin-right:18px}
.socials span{width:15px;height:15px;border:1.5px solid var(--white);border-radius:50%;display:block}
.brand{left:40px;top:42px;display:flex;align-items:center;gap:12px}
.brand-dot{width:40px;height:40px;border-radius:50%;background:var(--red)}
.brand-name{font-size:44px;font-weight:800;color:var(--blue);letter-spacing:1px;line-height:1}
.tagline{right:36px;top:82px;font-size:16px;font-weight:700;color:var(--blue)}
.tagline em{font-style:normal;color:var(--red)}

/* nav */
.main-nav{top:133px;height:42px;background:var(--blue);display:flex}
.main-nav a{position:absolute;top:0;height:42px;display:flex;align-items:center;gap:8px;color:var(--white);text-decoration:none;font-size:14px;font-weight:600;white-space:nowrap}
.main-nav a.active{background:var(--red);padding:0 24px}
.main-nav svg{width:15px;height:15px}

/* hero */
.hero{top:175px;height:512px;z-index:2}
.hero-photo{width:100%;height:100%;background:linear-gradient(105deg,#f4d7a8 0%,#9aa7ae 22%,#5c6b74 45%,#35454f 70%,#6f7c84 100%)}
.hero-banner{left:138px;top:490px;width:924px;height:46px;background:var(--red);border-radius:12px;color:var(--white);font-size:21px;font-weight:700;display:flex;align-items:center;justify-content:center;box-shadow:0 4px 8px rgba(0,0,0,.25);white-space:nowrap}

/* features */
.features{top:687px;height:208px;background:linear-gradient(#e6e6e6,#d9d9d9);z-index:1}
.feature{position:absolute;top:58px;display:flex;align-items:center;gap:24px}
.feature-icon{width:116px;height:116px;border-radius:50%;background:var(--red);display:flex;align-items:center;justify-content:center}
.feature-icon .inner{width:78px;height:78px;border-radius:50%;background:var(--blue);display:flex;align-items:center;justify-content:center;border:4px solid var(--white)}
.feature-icon svg{width:38px;height:38px}
.feature-label{font-size:15px;font-weight:700;color:var(--ink);text-align:center;line-height:1.25}

/* shared heading */
.section-title{position:absolute;left:0;width:1200px;display:flex;align-items:center;justify-content:center;gap:16px;font-size:30px;font-weight:700;color:var(--ink)}
.section-title em{color:var(--red);font-style:italic;font-weight:800}
.section-title .mark{width:38px;height:38px;border-radius:50%;background:var(--red)}
.section-title::before,.section-title::after{content:"";width:130px;height:1px;background:var(--rule)}

/* about */
.about{top:895px;height:415px;background:var(--white)}
.about-text{left:65px;top:125px;width:575px;font-size:12.5px;line-height:1.6;color:var(--muted)}
.about-text p+p{margin-top:16px}
.btn-more{left:68px;top:295px;width:232px;height:40px;background:var(--blue);border-radius:8px;color:var(--white);font-size:15px;font-weight:600;display:flex;align-items:center;justify-content:center;letter-spacing:.3px}
.about-photo{left:662px;top:115px;width:520px;height:265px;background:linear-gradient(160deg,#3c79c8 0%,#2a5fa6 55%,#c9a67a 80%,#e9e9e9 100%);border-radius:4px}

/* services */
.services{top:1310px;height:785px;background:linear-gradient(135deg,#e0e4fb 0%,#c7d0fb 50%,#dfe5fd 100%)}
.services-sub{left:0;top:128px;width:1200px;text-align:center;font-size:15px;font-weight:700;color:var(--ink)}
.hub-lines{left:0;top:0}
.hub{left:460px;top:248px;width:280px;height:280px;border-radius:50%;background:linear-gradient(#f4f4f4,#cfcfcf);display:flex;align-items:center;justify-content:center;box-shadow:0 4px 12px rgba(0,0,0,.15)}
.hub .core{width:220px;height:220px;border-radius:50%;background:var(--red)}
.node{width:124px;height:124px;border-radius:50%;background:linear-gradient(#fafafa,#d2d2d2);display:flex;align-items:center;justify-content:center;box-shadow:0 3px 8px rgba(0,0,0,.15)}
.node .inner{width:94px;height:94px;border-radius:50%;background:var(--blue);display:flex;align-items:center;justify-content:center}
.node svg{width:44px;height:44px}
.node-label{font-size:15px;font-weight:600;color:var(--ink);white-space:nowrap}

/* news */
.news{top:2095px;height:410px;background:var(--white)}
.news-card{position:absolute;top:152px;width:333px;height:205px}
.news-photo{width:333px;height:166px}
.news-bar{height:39px;background:var(--blue);display:flex;align-items:center;justify-content:space-between;color:var(--white);font-size:14px;font-weight:700}
.news-bar .title{padding-left:14px}
.news-bar .more{height:39px;background:#2b2b2b;padding:0 12px 0 14px;display:flex;align-items:center;gap:8px;font-weight:600;font-size:12px}
.date-badge{position:absolute;left:-10px;top:-52px;width:100px;height:100px;border-radius:50%;background:var(--blue);border:5px solid #e7e7e7;color:var(--white);text-align:center;font-weight:700;display:flex;flex-direction:column;justify-content:center;line-height:1.05}
.date-badge .m{font-size:14px}
.date-badge .d{font-size:30px}
.date-badge .y{font-size:13px}

/* testimonials */
.testimonials{top:2505px;height:410px;background:var(--grey-2)}
.quote-box{left:255px;top:132px;width:706px;height:148px;background:var(--white);border:1px solid #ddd;border-radius:8px;padding:20px 30px 0 62px;font-size:12.5px;line-height:1.55;color:var(--muted)}
.quote-box::after{content:"";position:absolute;left:40px;bottom:-12px;width:22px;height:22px;background:var(--white);border-right:1px solid #ddd;border-bottom:1px solid #ddd;transform:rotate(45deg)}
.quote-mark{font-size:48px;font-weight:800;color:#333;line-height:1;font-family:"Open Sans",Arial,sans-serif}
.quote-author{left:262px;top:303px;font-size:16px;font-weight:700;font-style:italic;color:var(--ink)}
.dots{left:0;top:352px;width:1200px;display:flex;justify-content:center;gap:6px}
.dots span{width:11px;height:11px;border-radius:50%;border:1.5px solid var(--blue)}
.dots span.on{background:var(--blue)}

/* footer */
.site-footer{top:2915px;height:245px;background:var(--blue);color:var(--white)}
.footer-brand{left:120px;top:146px;display:flex;align-items:center;gap:10px}
.footer-brand .brand-dot{width:30px;height:30px;background:var(--white)}
.footer-brand .brand-name{color:var(--white);font-size:34px}
.footer-col{position:absolute;top:42px}
.footer-col h4{font-size:14px;font-weight:700;padding-bottom:8px;border-bottom:1px solid rgba(255,255,255,.6);margin-bottom:14px}
.footer-col ul{list-style:none;font-size:12.5px;line-height:1.6}
.footer-col ul li::before{content:"- "}
.office-line{display:flex;gap:10px;font-size:13px;line-height:1.6;font-weight:600;margin-bottom:18px}
.office-line svg{flex:none;width:20px;height:20px}
.field{height:26px;background:var(--blue-dark);border:1px solid rgba(255,255,255,.4);font-size:10px;font-weight:600;padding:6px 10px;margin-bottom:4px}
.field.tall{height:56px}
.submit{display:inline-block;background:#111;font-size:12px;font-weight:700;padding:6px 22px;margin-top:4px}
.footer-bar{left:0;top:3160px;width:1200px;height:43px;background:var(--footer-bar);color:#ccc;font-size:11px;display:flex;align-items:center;padding:0 20px}
.footer-bar .socials{margin-right:0}
</style>
</head>
<body>

<header class="site-header">
  <div class="abs top-rule"></div>
  <div class="abs contact-strip">
    <span class="item"><svg width="18" height="18" viewBox="0 0 24 24"><circle cx="12" cy="12" r="11" fill="none" stroke="#fff" stroke-width="2"/><path d="M8 6l2 0 1 3-1.5 1a8 8 0 0 0 4 4l1-1.5 3 1 0 2a2 2 0 0 1-2 2A10 10 0 0 1 6 8a2 2 0 0 1 2-2z" fill="#fff"/></svg>1.800.555.0142</span>
    <span class="item"><svg width="18" height="18" viewBox="0 0 24 24"><circle cx="12" cy="12" r="11" fill="none" stroke="#fff" stroke-width="2"/><rect x="6" y="8" width="12" height="8" fill="none" stroke="#fff" stroke-width="1.6"/><path d="M6 8l6 5 6-5" fill="none" stroke="#fff" stroke-width="1.6"/></svg>hello@velmora-moves.com</span>
    <span class="socials"><span></span><span></span><span></span></span>
  </div>
  <div class="abs brand"><span class="brand-dot"></span><span class="brand-name">VELMORA</span></div>
  <div class="abs tagline">CONNECTING CARRIERS WITH CUSTOMERS <em>FOR SPECIALTY MOVES</em></div>
</header>

<nav class="main-nav">
  <a class="active" style="left:222px"><svg viewBox="0 0 16 16"><path d="M8 1L1 7h2v7h4v-4h2v4h4V7h2z" fill="#fff"/></svg>HOME</a>
  <a style="left:367px"><svg viewBox="0 0 16 16"><circle cx="8" cy="8" r="6" fill="none" stroke="#fff" stroke-width="2"/></svg>ABOUT</a>
  <a style="left:495px"><svg viewBox="0 0 16 16"><circle cx="8" cy="8" r="3" fill="none" stroke="#fff" stroke-width="2"/><path d="M8 1v3M8 12v3M1 8h3M12 8h3M3 3l2 2M11 11l2 2M13 3l-2 2M5 11l-2 2" stroke="#fff" stroke-width="1.6"/></svg>SERVICES</a>
  <a style="left:640px"><svg viewBox="0 0 16 16"><path d="M2 3h12v8H7l-3 3v-3H2z" fill="none" stroke="#fff" stroke-width="1.6"/></svg>TESTIMONIALS</a>
  <a style="left:788px"><svg viewBox="0 0 16 16"><rect x="2" y="3" width="12" height="10" fill="none" stroke="#fff" stroke-width="1.6"/><path d="M4 6h8M4 9h8" stroke="#fff" stroke-width="1.4"/></svg>NEWS</a>
  <a style="left:903px"><svg viewBox="0 0 16 16"><circle cx="8" cy="5" r="3" fill="#fff"/><path d="M2 15a6 6 0 0 1 12 0z" fill="#fff"/></svg>CONTACT</a>
</nav>

<section class="hero">
  <div class="hero-photo" role="img" aria-label="Photo of a truck driving at speed on a highway under a cloudy sky"></div>
  <div class="abs hero-banner">WE CONNECT CARRIERS WITH CUSTOMERS FOR SPECIALTY MOVES</div>
</section>

<section class="features">
  <div class="feature" style="left:48px">
    <div class="feature-icon"><div class="inner"><svg viewBox="0 0 24 24"><rect x="3" y="4" width="16" height="16" fill="none" stroke="#fff" stroke-width="2.2"/><path d="M7 12l4 4 10-12" fill="none" stroke="#fff" stroke-width="2.6"/></svg></div></div>
    <div class="feature-label">INDUSTRY<br>LEADER</div>
  </div>
  <div class="feature" style="left:312px">
    <div class="feature-icon"><div class="inner"><svg viewBox="0 0 24 24"><path d="M4 13a8 8 0 0 1 16 0" fill="none" stroke="#fff" stroke-width="2.2"/><rect x="2" y="12" width="4" height="6" rx="1" fill="#fff"/><rect x="18" y="12" width="4" height="6" rx="1" fill="#fff"/><path d="M20 18v2h-6" fill="none" stroke="#fff" stroke-width="1.8"/></svg></div></div>
    <div class="feature-label">QUALITY<br>CUSTOMER<br>SERVICE</div>
  </div>
  <div class="feature" style="left:586px">
    <div class="feature-icon"><div class="inner"><svg viewBox="0 0 24 24"><rect x="2" y="6" width="13" height="10" fill="none" stroke="#fff" stroke-width="2"/><path d="M15 9h4l3 4v3h-7z" fill="none" stroke="#fff" stroke-width="2"/><circle cx="6" cy="18" r="2" fill="#fff"/><circle cx="18" cy="18" r="2" fill="#fff"/></svg></div></div>
    <div class="feature-label">QUALITY<br>TRANSPORTATION</div>
  </div>
  <div class="feature" style="left:910px">
    <div class="feature-icon"><div class="inner"><svg viewBox="0 0 24 24"><path d="M12 2a7 7 0 0 0-7 7c0 5 7 13 7 13s7-8 7-13a7 7 0 0 0-7-7z" fill="none" stroke="#fff" stroke-width="2"/><circle cx="12" cy="9" r="2.6" fill="#fff"/></svg></div></div>
    <div class="feature-label">ADVANCED<br>TECHNOLOGY</div>
  </div>
</section>

<section class="about">
  <h2 class="section-title" style="top:56px"><span class="mark"></span>ABOUT <em>VELMORA</em></h2>
  <div class="abs about-text">
    <p>Lorem ipsum dolor sit amet, consectetuer adipiscing elit, sed diam nonummy nibh euismod tincidunt ut laoreet dolore magna aliquam erat volutpat. Ut wisi enim ad minim veniam, quis nostrud exerci tation ullamcorper suscipit lobortis nisl ut aliquip ex ea commodo consequat.</p>
    <p>Duis autem vel eum iriure dolor in hendrerit in vulputate velit esse molestie consequat, vel illum dolore eu feugiat nulla facilisis at vero eros et accumsan et iusto odio dignissim qui blandit praesent luptatum zzril delenit augue duis dolore te feugait nulla facilisi.</p>
  </div>
  <div class="abs btn-more">MORE ABOUT US</div>
  <div class="abs about-photo" role="img" aria-label="Photo of a blue shipping container with stacked cardboard boxes in front"></div>
</section>

<section class="services">
  <h2 class="section-title" style="top:50px"><span class="mark"></span>OUR <em>SERVICES</em></h2>
  <div class="abs services-sub">We connect carriers with customers that need specialty moves for</div>
  <svg class="abs hub-lines" width="1200" height="785" viewBox="0 0 1200 785">
    <g stroke="#d9d9dc" stroke-width="16" stroke-linecap="round">
      <line x1="600" y1="388" x2="335" y2="241"/>
      <line x1="600" y1="388" x2="872" y2="234"/>
      <line x1="600" y1="388" x2="335" y2="497"/>
      <line x1="600" y1="388" x2="872" y2="497"/>
      <line x1="600" y1="388" x2="600" y2="661"/>
    </g>
  </svg>
  <div class="abs hub"><div class="core"></div></div>

  <div class="abs node" style="left:273px;top:179px"><div class="inner"><svg viewBox="0 0 24 24"><rect x="4" y="18" width="10" height="3" fill="#fff"/><path d="M9 18V11l7-5 3 3" fill="none" stroke="#fff" stroke-width="2.2"/><circle cx="9" cy="11" r="1.8" fill="#fff"/></svg></div></div>
  <div class="abs node-label" style="left:52px;top:230px">MANUFACTURING EQUIPMENT</div>

  <div class="abs node" style="left:810px;top:172px"><div class="inner"><svg viewBox="0 0 24 24"><path d="M3 9l2-5h14l2 5z" fill="#fff"/><rect x="5" y="10" width="14" height="10" fill="none" stroke="#fff" stroke-width="2"/><rect x="10" y="14" width="4" height="6" fill="#fff"/></svg></div></div>
  <div class="abs node-label" style="left:945px;top:224px">STORE FIXTURES</div>

  <div class="abs node" style="left:273px;top:435px"><div class="inner"><svg viewBox="0 0 24 24"><rect x="3" y="4" width="15" height="11" fill="none" stroke="#fff" stroke-width="2"/><rect x="14" y="9" width="7" height="11" rx="1" fill="#0b5f96" stroke="#fff" stroke-width="2"/><path d="M8 19h5" stroke="#fff" stroke-width="2"/></svg></div></div>
  <div class="abs node-label" style="left:164px;top:488px">TECHNOLOGY</div>

  <div class="abs node" style="left:810px;top:435px"><div class="inner"><svg viewBox="0 0 24 24"><rect x="3" y="5" width="18" height="12" fill="none" stroke="#fff" stroke-width="2"/><path d="M6 14v-3M9 14V9M12 14v-4M15 14V8M18 14v-2" stroke="#fff" stroke-width="1.6"/><path d="M8 21l4-4 4 4" fill="none" stroke="#fff" stroke-width="2"/></svg></div></div>
  <div class="abs node-label" style="left:945px;top:488px">DISPLAYS</div>

  <div class="abs node" style="left:538px;top:599px"><div class="inner"><svg viewBox="0 0 24 24"><rect x="9" y="3" width="6" height="8" rx="1" fill="#fff"/><rect x="5" y="11" width="14" height="4" fill="#fff"/><path d="M5 18h14" stroke="#fff" stroke-width="2"/></svg></div></div>
  <div class="abs node-label" style="left:676px;top:652px">EXHIBITS</div>
</section>

<section class="news">
  <h2 class="section-title" style="top:56px"><span class="mark"></span>LATEST <em>NEWS</em></h2>
  <article class="news-card" style="left:79px">
    <div class="news-photo" role="img" aria-label="Photo of a city highway at dusk with motion blur" style="background:linear-gradient(120deg,#2b3a52,#5a6f8c 55%,#1e2636)"></div>
    <div class="news-bar"><span class="title">News Title #1</span><span class="more">READ MORE ›</span></div>
    <div class="date-badge"><span class="m">OCT</span><span class="d">16</span><span class="y">2016</span></div>
  </article>
  <article class="news-card" style="left:445px">
    <div class="news-photo" role="img" aria-label="Photo of red truck trailers parked at sunset" style="background:linear-gradient(120deg,#e2b56a,#a23a2c 45%,#4a3a3a)"></div>
    <div class="news-bar"><span class="title">News Title #2</span><span class="more">READ MORE ›</span></div>
    <div class="date-badge"><span class="m">OCT</span><span class="d">08</span><span class="y">2016</span></div>
  </article>
  <article class="news-card" style="left:808px">
    <div class="news-photo" role="img" aria-label="Photo of a hand using a tablet showing charts" style="background:linear-gradient(120deg,#f2f2f2,#d8d2c8 55%,#b7b0a6)"></div>
    <div class="news-bar"><span class="title">News Title #3</span><span class="more">READ MORE ›</span></div>
    <div class="date-badge"><span class="m">OCT</span><span class="d">06</span><span class="y">2016</span></div>
  </article>
</section>

<section class="testimonials">
  <h2 class="section-title" style="top:56px"><span class="mark"></span>WORDS FROM <em>HAPPY CUSTOMERS</em></h2>
  <div class="abs quote-box">
    <span class="abs quote-mark" style="left:16px;top:12px">“</span>
    Lorem ipsum dolor sit amet, consectetuer adipiscing elit, sed diam nonummy nibh euismod tincidunt ut laoreet dolore magna aliquam erat volutpat. Ut wisi enim ad minim veniam, quis nostrud exerci tation ullamcorper suscipit lobortis nisl ut aliquip ex ea commodo consequat. Duis autem vel eum iriure dolor in hendrerit in vulputate velit esse molestie consequat, vel illum dolore eu feugiat nulla facilisis at vero. <span class="quote-mark" style="font-size:40px;line-height:0;vertical-align:-14px">”</span>
  </div>
  <div class="abs quote-author">Maren Holt</div>
  <div class="abs dots"><span class="on"></span><span></span><span></span><span></span></div>
</section>

<footer class="site-footer">
  <div class="abs footer-brand"><span class="brand-dot"></span><span class="brand-name">VELMORA</span></div>
  <div class="footer-col" style="left:425px;width:100px">
    <h4>QUICK LINKS</h4>
    <ul><li>Home</li><li>About</li><li>Services</li><li>Testimonials</li><li>News</li><li>Contact</li></ul>
  </div>
  <div class="footer-col" style="left:605px;width:200px">
    <h4>HEAD OFFICE</h4>
    <div class="office-line"><svg viewBox="0 0 24 24"><circle cx="12" cy="12" r="10" fill="none" stroke="#fff" stroke-width="2"/><circle cx="12" cy="10" r="3" fill="#fff"/><path d="M12 13v5" stroke="#fff" stroke-width="2"/></svg><span>VELMORA<br>48 Alder Park Dr<br>Pasadena, CA 91101</span></div>
    <div class="office-line"><svg viewBox="0 0 24 24"><circle cx="12" cy="12" r="10" fill="none" stroke="#fff" stroke-width="2"/><path d="M8 7h2l1 3-1.5 1a7 7 0 0 0 3.5 3.5l1-1.5 3 1v2a2 2 0 0 1-2 2A9 9 0 0 1 6 9a2 2 0 0 1 2-2z" fill="#fff"/></svg><span>Toll Free: 1-800-555-0142</span></div>
    <div class="office-line"><svg viewBox="0 0 24 24"><circle cx="12" cy="12" r="10" fill="none" stroke="#fff" stroke-width="2"/><rect x="7" y="8.5" width="10" height="7" fill="none" stroke="#fff" stroke-width="1.6"/><path d="M7 8.5l5 4 5-4" fill="none" stroke="#fff" stroke-width="1.6"/></svg><span>hello@velmora-moves.com</span></div>
  </div>
  <div class="footer-col" style="left:874px;width:226px">
    <h4>QUICK MESSAGE</h4>
    <div class="field">NAME</div>
    <div class="field">EMAIL</div>
    <div class="field tall">MESSAGE</div>
    <span class="submit">SUBMIT</span>
  </div>
</footer>
<div class="abs footer-bar">© 2016 VELMORA. ALL RIGHTS RESERVED.<span class="socials" style="margin-left:auto"><span style="border-color:#ccc"></span><span style="border-color:#ccc"></span><span style="border-color:#ccc"></span></span></div>

</body>
</html>
```